Pregnancy and Fertility Information Website

Hello Designers,
I need a website which provide tips and information about healthy and happy pregnancy. My website name is Lorvin medical.

The website should provide all the information needed throughout pregnancy and beyond ranging from pregnancy tracking tools and articles about common pregnancy concerns and what to expect during pregnancy,etc.
The details about first trimester, second trimester and third trimester should be highlighted in the website.

Top Navigation
Home, Fertility, Pregnancy basics, Articles, Tips and News

I'm looking for a simple and clean design which involves captivating images and colors but it shouldn't be crowded. The design must be professional and modern. An easy to navigate layout is a must.

Green, violet, blue and light yellow colors are my favorites but i'm open to other options.

Any questions. Kindly ask

Industry/Entity Type

Medical

```html
<!DOCTYPE html>
<html lang="en">
<head>
<meta charset="utf-8">
<title>Lorvin Medical — Pregnancy &amp; Fertility</title>
<link href="https://fonts.googleapis.com/css2?family=Source+Sans+3:ital,wght@0,400;0,600;0,700;1,400&display=swap" rel="stylesheet">
<style>
:root{
  --green:#5bb846;
  --green-dark:#3f9e3a;
  --blue:#1f78b4;
  --teal:#2a9aa8;
  --text:#3c3c3c;
  --muted:#6b6b6b;
  --white:#ffffff;
  --band-start:#cfe8c6;
  --band-end:#a5d3de;
  --line:#d4d4d4;
  --field:#f7f7f7;
}
*{box-sizing:border-box;margin:0;padding:0}
html,body{width:1200px;height:3814px;overflow:hidden}
body{font-family:"Source Sans 3",Arial,sans-serif;color:var(--text);background:var(--white);position:relative}
section,header,footer{position:absolute;left:0;width:1200px}
.abs{position:absolute}
p{font-size:14px;line-height:1.55}

/* Top bar */
.topbar{top:0;height:71px;background:linear-gradient(90deg,var(--green),var(--blue));color:var(--white)}
.topbar .phone{left:140px;top:24px;display:flex;align-items:center;gap:10px;font-size:15px}
.topbar nav{left:448px;top:24px;display:flex;gap:36px;font-size:16px}
.topbar nav a{color:rgba(255,255,255,.7);text-decoration:none}
.topbar nav a.current{color:var(--white)}
.topbar .tools{left:1008px;top:24px;display:flex;gap:16px}

/* Hero */
.hero{top:71px;height:425px;background:linear-gradient(100deg,#f4f3f1 0%,#ecebe8 45%,#dedad4 75%,#cfc8bf 100%)}
.hero .photo{left:560px;top:0;width:640px;height:425px;background:linear-gradient(90deg,rgba(236,235,232,0) 0%,#d9d2c8 55%,#c8bdb1 100%)}
.brand{left:140px;top:18px;width:242px;height:242px;border-radius:50%;background:var(--white);display:flex;flex-direction:column;align-items:center;justify-content:center;gap:14px}
.brand .dot{width:52px;height:52px;border-radius:50%;background:var(--blue)}
.brand .name{font-size:28px;font-weight:600;color:var(--blue)}
.tagline{left:140px;top:268px;font-size:34px;line-height:1.1;color:var(--green);font-weight:400}
.tagline b{font-weight:700}
.hero-btns{left:142px;top:369px;display:flex;gap:24px}
.btn{display:flex;align-items:center;justify-content:center;gap:10px;height:40px;border-radius:20px;background:var(--green);color:var(--white);font-size:15px}
.hero-btns .btn{width:164px}

/* Trimesters */
.trimesters{top:496px;height:470px;background:linear-gradient(90deg,var(--green) 0%,var(--teal) 55%,var(--blue) 100%);color:var(--white)}
.silhouette{top:25px;width:110px;height:228px;border-radius:55px 55px 20px 20px;background:linear-gradient(180deg,rgba(20,70,90,.55),rgba(20,70,90,.35))}
.tabs{left:145px;top:267px;width:910px;display:flex;justify-content:space-between}
.tab{width:153px;height:38px;border-radius:19px;background:rgba(255,255,255,.35);display:flex;align-items:center;justify-content:center;font-size:14px;color:var(--white)}
.tab.active{background:var(--white);color:var(--green-dark)}
.trimesters p{left:140px;top:328px;width:920px;color:var(--white)}
.read-more{font-size:10px;letter-spacing:.5px;text-transform:uppercase;color:var(--text)}
.trimesters .read-more{left:140px;top:425px;color:var(--white)}

/* Split sections */
.split-title{display:flex;align-items:center;gap:12px;font-size:36px;font-weight:400;color:var(--green);line-height:1}
.split p{width:440px}
.photo-fill{top:0;height:100%}

.fertility{top:966px;height:394px}
.fertility h2{left:140px;top:50px}
.fertility .body{left:140px;top:100px}
.fertility .photo-fill{left:623px;width:577px;background:linear-gradient(135deg,#efe2d8,#d9b8a4 50%,#3a4a6a 100%)}

.pregnancy{top:1622px;height:392px}
.pregnancy .photo-fill{left:0;width:580px;background:linear-gradient(120deg,#dcd6d0,#efece8 45%,#d8e2ea 100%)}
.pregnancy h2{left:623px;top:45px}
.pregnancy .body{left:623px;top:98px}

.tips{top:2296px;height:392px}
.tips .photo-fill{left:623px;width:577px;background:linear-gradient(160deg,#f2ece6,#f0d6cc 45%,#e8e2da 100%)}
.tips h2{left:140px;top:45px}
.tips ul{left:140px;top:98px;list-style:none}
.tips li{display:flex;align-items:center;gap:12px;font-size:14px;height:33px}
.tips li::before{content:"";width:9px;height:9px;border-radius:50%;background:var(--green);flex:none}

/* Pale bands */
.band{background:linear-gradient(90deg,var(--band-start),var(--band-end))}
.band h2{left:0;width:1200px;justify-content:center;color:#3d5a66}
.dots{display:flex;gap:8px;left:0;width:1200px;justify-content:center}
.dots span{width:11px;height:11px;border-radius:50%;background:rgba(255,255,255,.75)}
.dots span.on{background:#7fb3c0}

.testimonials{top:1360px;height:262px}
.testimonials h2{top:48px}
.testimonials .quote{left:260px;top:98px;width:680px;text-align:center;font-style:italic;font-size:14px}
.testimonials .author{left:0;top:162px;width:1200px;text-align:center;font-size:13px}
.testimonials .dots{top:216px}

.articles{top:2014px;height:282px}
.articles h2{top:48px}
.articles h3{left:224px;top:102px;font-size:19px;font-weight:700;color:#2b2b2b}
.articles p{left:224px;top:128px;width:790px;font-size:13px}
.articles .read-more{left:224px;top:196px}
.articles .dots{top:230px}

.news{top:2688px;height:282px}
.news h2{top:48px}
.date{left:224px;top:102px;width:90px;text-align:center;color:#2b2b2b}
.date .day{font-size:26px;line-height:1;border-bottom:1px solid #2b2b2b;padding-bottom:4px}
.date .year{font-size:36px;font-weight:700;line-height:1.1}
.news h3{left:332px;top:100px;font-size:19px;font-weight:700;color:#2b2b2b}
.news p{left:332px;top:126px;width:690px;font-size:13px}
.news .read-more{left:332px;top:206px}
.news .dots{top:234px}

/* Contact */
.contact{top:2970px;height:496px}
.contact h2{left:140px;top:40px}
.field{left:140px;width:440px;height:43px;border:1px solid var(--line);background:var(--field);font-size:13px;color:var(--muted);padding:12px 14px}
.field.name{top:107px}
.field.email{top:166px}
.field.message{top:224px;height:163px}
.contact .send{left:140px;top:402px;width:173px;height:43px;border-radius:22px;font-size:16px;font-weight:600;letter-spacing:.5px}
.contact .intro{left:623px;top:105px;width:435px;font-size:13px}
.contact .address{left:623px;top:220px;font-size:13px;line-height:1.5}
.socials{left:623px;top:350px;display:flex;gap:18px}
.socials span{width:48px;height:48px;border-radius:50%;border:2px solid var(--green)}

.map{top:3466px;height:280px;background:linear-gradient(120deg,#e6e6e6,#d6d6d6 50%,#e2e2e2)}
.site-footer{top:3746px;height:68px;background:linear-gradient(90deg,var(--green),var(--blue));color:var(--white);font-size:12px;display:flex;align-items:center;justify-content:center}
</style>
</head>
<body>

<header class="topbar">
  <div class="abs phone">
    <svg width="18" height="18" viewBox="0 0 24 24" fill="none" stroke="#fff" stroke-width="2"><path d="M5 3h4l2 5-3 2a12 12 0 0 0 6 6l2-3 5 2v4a2 2 0 0 1-2 2A17 17 0 0 1 3 5a2 2 0 0 1 2-2z"/></svg>
    +000 (0)00000000
  </div>
  <nav class="abs">
    <a class="current" href="#">Home</a><a href="#">Fertility</a><a href="#">Pregnancy</a><a href="#">Articles</a><a href="#">Tips</a><a href="#">News</a>
  </nav>
  <div class="abs tools">
    <svg width="22" height="18" viewBox="0 0 24 18" fill="none" stroke="#fff" stroke-width="2"><rect x="1" y="1" width="22" height="16"/><path d="M1 1l11 9 11-9"/></svg>
    <svg width="18" height="18" viewBox="0 0 24 24" fill="none" stroke="#fff" stroke-width="2"><circle cx="18" cy="5" r="3"/><circle cx="6" cy="12" r="3"/><circle cx="18" cy="19" r="3"/><path d="M9 11l6-4M9 13l6 4"/></svg>
  </div>
</header>

<section class="hero">
  <div class="abs photo" role="img" aria-label="Photo of a smiling pregnant woman holding her belly in a bright bedroom"></div>
  <div class="abs brand"><span class="dot"></span><span class="name">Lorvin medical</span></div>
  <h1 class="abs tagline"><b style="font-weight:400">Mother</b><b>hood</b> offers<br>a dream of <b>possibilities...</b></h1>
  <div class="abs hero-btns">
    <span class="btn"><svg width="16" height="16" viewBox="0 0 24 24" fill="none" stroke="#fff" stroke-width="2"><rect x="3" y="5" width="18" height="16"/><path d="M3 10h18M8 2v5M16 2v5"/></svg>Apointments</span>
    <span class="btn"><svg width="16" height="16" viewBox="0 0 24 24" fill="none" stroke="#fff" stroke-width="2"><circle cx="12" cy="12" r="9"/><path d="M12 7v5l3 3"/></svg>Schedule</span>
  </div>
</section>

<section class="trimesters">
  <div class="abs silhouette" style="left:166px" role="img" aria-label="Silhouette of a woman in the first trimester"></div>
  <div class="abs silhouette" style="left:420px" role="img" aria-label="Silhouette of a woman in the second trimester"></div>
  <div class="abs silhouette" style="left:672px" role="img" aria-label="Silhouette of a woman in the third trimester"></div>
  <div class="abs silhouette" style="left:923px" role="img" aria-label="Silhouette of a mother lifting her baby"></div>
  <div class="abs tabs">
    <span class="tab active">1 Trimester</span><span class="tab">2 Trimester</span><span class="tab">3 Trimester</span><span class="tab">Birth</span>
  </div>
  <p class="abs">Lorem ipsum dolor sit amet, consectetur adipiscing elit. Fusce vitae dui id nulla suscipit sagittis. Pellentesque gravida, leo ut ullamcorper cursus, lacus nulla sodales elit, non sollicitudin lectus mauris et metus. Mauris facilisis convallis vehicula. Morbi eget sem ligula. Proin porttitor leo a nisi hendrerit tristique. Vestibulum lacinia consectetur eros ac sagittis. Proin id urna tincidunt, suscipit ex eget, condimentum felis. Maecenas viverra lectus ut sapien aliquam dapibus. Vestibulum eleifend, turpis sit amet cursus congue, est augue rutrum justo.</p>
  <span class="abs read-more">Read more</span>
</section>

<section class="fertility split">
  <h2 class="abs split-title"><svg width="34" height="26" viewBox="0 0 34 26" fill="none" stroke="#5bb846" stroke-width="2.5"><path d="M2 13h18M8 6h14M8 20h14"/><circle cx="27" cy="13" r="5"/></svg>Fertility</h2>
  <div class="abs body">
    <p>Lorem ipsum dolor sit amet, consectetur adipiscing elit. Vestibulum sed nulla ligula. In ornare quam sed ex eleifend semper. Praesent et elit tempor risus mattis ultricies at non ipsum. Nulla scelerisque, mauris iaculis elementum porta, erat nunc pharetra turpis, eget malesuada diam massa in nunc. Morbi interdum elit leo, vitae accumsan magna scelerisque fermentum.</p>
    <p style="margin-top:14px">Pellentesque habitant morbi tristique senectus et netus et malesuada fames ac turpis egestas. Aliquam tempus justo non neque porta euismod. Sed et eros ac dui pretium bibendum sit amet fringilla orci. Etiam condimentum elit sit amet sem dapibus ornare. Suspendisse pulvinar nisi eget nulla vestibulum molestie. Nulla ac sapien tempus, posuere libero non, efficitur dolor.</p>
  </div>
  <div class="abs photo-fill" role="img" aria-label="Photo of a pregnant belly with a pair of baby shoes held beside it"></div>
</section>

<section class="testimonials band">
  <h2 class="abs split-title"><svg width="34" height="28" viewBox="0 0 34 28" fill="none" stroke="#3d5a66" stroke-width="2.5"><path d="M3 3h28v16H14l-7 6v-6H3z"/></svg>Testimonials</h2>
  <p class="abs quote">“Morbi quis varius ex, a viverra diam. Sed non purus in sem finibus varius. Mauris vel odio quis mauris congue convallis. Nullam imperdiet nec purus sed elementum. Curabitur ac eleifend ipsum, sodales vestibulum sapien.”</p>
  <span class="abs author">Mrs. Clara Benet</span>
  <div class="abs dots"><span class="on"></span><span></span><span></span><span></span><span></span><span></span></div>
</section>

<section class="pregnancy split">
  <div class="abs photo-fill" role="img" aria-label="Photo of a doctor with a clipboard talking with a pregnant patient lying in bed"></div>
  <h2 class="abs split-title"><svg width="34" height="28" viewBox="0 0 34 28" fill="none" stroke="#5bb846" stroke-width="2.5"><path d="M3 24C10 24 18 18 20 8l10-5-4 9c-2 8-10 12-23 12z"/></svg>Pregnancy</h2>
  <div class="abs body">
    <p>Lorem ipsum dolor sit amet, consectetur adipiscing elit. Fusce vitae dui id nulla suscipit sagittis. Pellentesque gravida, leo ut ullamcorper cursus, lacus nulla sodales elit, non sollicitudin lectus mauris et metus. Mauris facilisis convallis vehicula. Morbi eget sem ligula. Proin porttitor leo a nisi hendrerit tristique. Vestibulum lacinia consectetur eros ac sagittis. Proin id urna tincidunt, suscipit ex eget, condimentum felis.</p>
    <p style="margin-top:14px">Etiam condimentum elit sit amet sem dapibus ornare. Suspendisse pulvinar nisi eget nulla vestibulum molestie. Nulla ac sapien tempus, posuere libero non, efficitur dolor. Sed consequat, ante in lacinia viverra, mi tortor accumsan arcu, sit amet vehicula mi ex sed metus. Nunc bibendum et lacus eu tristique. Maecenas viverra lectus ut sapien aliquam dapibus. Vestibulum eleifend, turpis sit amet cursus congue.</p>
  </div>
</section>

<section class="articles band">
  <h2 class="abs split-title"><svg width="26" height="30" viewBox="0 0 26 30" fill="none" stroke="#3d5a66" stroke-width="2.5"><path d="M3 2h14l6 6v20H3z"/><path d="M8 13h10M8 18h10M8 23h10"/></svg>Articles</h2>
  <h3 class="abs">Vivamus a metus sed libero vehicula euismod</h3>
  <p class="abs">Nunc pulvinar aliquet quam sed consectetur. Mauris vestibulum vel libero sed aliquet. Sed urna dolor, mattis eu massa non, aliquam sollicitudin nulla. Suspendisse sagittis lorem nunc. Mauris elit quam, euismod quis ex sodales, luctus dignissim enim. Nam ultrices dui ut lectus tincidunt consectetur. Nunc malesuada congue augue ...</p>
  <span class="abs read-more">Read more</span>
  <div class="abs dots"><span></span><span></span><span class="on"></span><span></span><span></span><span></span></div>
</section>

<section class="tips split">
  <h2 class="abs split-title"><svg width="30" height="30" viewBox="0 0 30 30" fill="none" stroke="#5bb846" stroke-width="2.5"><circle cx="15" cy="15" r="12"/><path d="M15 13v9M15 8v1"/></svg>Tips</h2>
  <ul class="abs">
    <li>Etiam ullamcorper augue quis ex consectetur commodo.</li>
    <li>Fusce vitae eros eget mauris cursus tempus a ut quam.</li>
    <li>Etiam maximus odio at elit bibendum rhoncus.</li>
    <li>Duis in ligula gravida, bibendum turpis in, aliquam erat.</li>
    <li>Vivamus in erat malesuada, laoreet ex at, volutpat leo.</li>
    <li>Phasellus gravida nibh quis purus consectetur ipsum finibus.</li>
    <li>Aenean facilisis sem facilisis, tempus dui in, iaculis justo.</li>
  </ul>
  <div class="abs photo-fill" role="img" aria-label="Photo of a pregnant woman preparing a healthy breakfast with milk, fruit and cereal"></div>
</section>

<section class="news band">
  <h2 class="abs split-title"><svg width="32" height="28" viewBox="0 0 32 28" fill="none" stroke="#3d5a66" stroke-width="2.5"><path d="M3 10h6l14-7v22L9 18H3z"/><path d="M9 18l2 8"/></svg>News</h2>
  <div class="abs date"><div class="day">25 FEB</div><div class="year">2017</div></div>
  <h3 class="abs">Mauris vestibulum vel libero sed aliquet</h3>
  <p class="abs">Sed urna dolor, mattis eu massa non, aliquam sollicitudin nulla. Suspendisse sagittis lorem nunc. Mauris elit quam, euismod quis ex sodales, luctus dignissim enim. Nam ultrices dui ut lectus tincidunt consectetur. Nunc malesuada congue augue, quis lobortis mi consectetur luctus ...</p>
  <span class="abs read-more">Read more</span>
  <div class="abs dots"><span></span><span class="on"></span><span></span><span></span><span></span><span></span></div>
</section>

<section class="contact">
  <h2 class="abs split-title"><svg width="34" height="26" viewBox="0 0 34 26" fill="none" stroke="#5bb846" stroke-width="2.5"><path d="M2 10L17 2l15 8v14H2z"/><path d="M2 10l15 9 15-9"/></svg>Contact</h2>
  <div class="abs field name">Your full name</div>
  <div class="abs field email">Your email address</div>
  <div class="abs field message">Your message</div>
  <span class="abs btn send">SEND</span>
  <p class="abs intro">Lorem ipsum dolor sit amet, consectetur adipiscing elit. Pellentesque vehicula diam tortor, vel blandit mauris tempus et. Sed ultrices feugiat lacus. Nulla egestas quam vel interdum ultrices. Aenean sodales est nulla, nec vulputate odio scelerisque a. Quisque quis volutpat diam.</p>
  <div class="abs address">Lorvin Medical<br>Street name, City, Country<br>Tel : +000 (0)00000000 &nbsp;|&nbsp; Mob : +000 (0)00000000<br>Email: info@lorvinmedical.com</div>
  <div class="abs socials"><span></span><span></span><span></span><span></span></div>
</section>

<section class="map" role="img" aria-label="Street map showing the clinic location"></section>

<footer class="site-footer">Copyright © Lorvin Medical. All rights reserved.</footer>

</body>
</html>
```